clean web design for a recruitment company

We need a web design for a company called 'TORAVI' recruitment. We are a new age recruitment companies that selects people by their true nature, values and what they can bring to the table as a tangible talent. We are all here possessing a certain talent, whatever that could be that the world needs. The final design should communicate professionalism and strongly embedded etiquette we believe in and a branding promise 'Seeing ones true nature'. Our companies values are integrity, giving away to the community, cherishing the sharing of our talent, time and helping one another.

Target Market(s)

Gulf Countries

Industry/Entity Type

It Company

Number of Pages Required

1 page

Font styles to use
Serif

Requirements
Must have
• Clear and readable font, user friendly structure and easy navigation menus.
Nice to have
• Extra sort of ideas on images we may use, tag lines etc. sample sites we love site:https://www.velmaroque.com/
• http://www.dorisaklund.com/
• http://www.pebblemoorhouse.com/idea-gallery/
Should not have
• all sort of colors, big combination of fonts, images with people in the office or people in suits likewise all the typical industry web sites

```html
<!DOCTYPE html>
<html lang="en">
<head>
<meta charset="utf-8">
<title>Toravi Recruitment</title>
<link rel="stylesheet" href="https://fonts.googleapis.com/css2?family=Lato:wght@300;400;700;900&display=swap">
<style>
  :root {
    --ink: #1f1f21;
    --ink-soft: #4a4a4d;
    --paper: #ffffff;
    --backdrop: #f1f1f1;
    --accent: #ff1464;
    --photo-cool: #5f6a80;
    --photo-mid: #7d7680;
    --photo-warm: #8a6a5c;
    --band: #3c4458;
  }
  * { margin: 0; padding: 0; box-sizing: border-box; }
  html, body { width: 1200px; height: 1000px; overflow: hidden; background: var(--backdrop); }
  body { font-family: "Lato", Arial, sans-serif; color: var(--ink); position: relative; }

  /* Website */
  .site { position: absolute; left: 0; top: 0; width: 1200px; height: 640px; background: var(--paper); overflow: hidden; }
  .site-header { position: absolute; left: 0; top: 0; width: 100%; height: 82px; display: flex; align-items: center; padding: 0 150px 0 150px; }
  .brand { display: flex; align-items: center; gap: 10px; font-weight: 900; font-size: 30px; letter-spacing: 0.5px; color: var(--ink); }
  .brand-square { width: 14px; height: 14px; background: var(--ink); }
  .main-nav { margin-left: auto; display: flex; align-items: center; gap: 26px; font-size: 13px; font-weight: 400; }
  .main-nav a { color: var(--ink); text-decoration: none; }
  .main-nav .is-active { border: 3px solid var(--ink); padding: 8px 14px; font-weight: 700; }

  .hero-photo { position: absolute; left: 300px; top: 82px; width: 900px; height: 558px;
    background: linear-gradient(100deg, var(--photo-cool) 0%, var(--photo-mid) 45%, var(--photo-warm) 100%); }
  .hero-band { position: absolute; left: 300px; top: 590px; width: 380px; height: 50px; background: var(--band); }

  .hero-card { position: absolute; left: 150px; top: 290px; width: 530px; height: 300px; background: var(--paper); padding: 24px 20px 0 30px; }
  .hero-title { font-size: 76px; line-height: 1; font-weight: 900; letter-spacing: -1px; }
  .hero-subtitle { font-size: 76px; line-height: 1; font-weight: 300; color: var(--ink-soft); }
  .hero-copy { margin-top: 22px; font-size: 14px; line-height: 1.5; color: var(--ink-soft); text-align: justify; max-width: 470px; }

  /* Brand mark */
  .brand-lockup { position: absolute; left: 0; top: 672px; width: 100%; display: flex; justify-content: center; align-items: center; gap: 16px; }
  .brand-lockup .brand-square { width: 26px; height: 26px; }
  .brand-lockup .brand-name { font-size: 64px; font-weight: 900; letter-spacing: 2px; line-height: 1; }

  /* Team portraits */
  .team { position: absolute; left: 0; top: 782px; width: 100%; display: flex; justify-content: center; gap: 90px; }
  .portrait { width: 160px; height: 180px; border-radius: 80px 80px 40px 40px; }
  .portrait--dark { background: linear-gradient(180deg, #2a2a2c, #5a5a5e); }
  .portrait--accent { background: linear-gradient(180deg, var(--accent), #ff6b9b); }
</style>
</head>
<body>
  <section class="site">
    <header class="site-header">
      <div class="brand"><span class="brand-square"></span>toravi</div>
      <nav class="main-nav">
        <a class="is-active" href="#">Home</a>
        <a href="#">Team</a>
        <a href="#">Methodology</a>
        <a href="#">Specialist Areas</a>
        <a href="#">Clients</a>
        <a href="#">Candidates</a>
        <a href="#">Toravi group</a>
      </nav>
    </header>

    <div class="hero-photo" role="img" aria-label="Photo of a person in a knit sweater holding a lit sparkler"></div>
    <div class="hero-band"></div>

    <div class="hero-card">
      <h1 class="hero-title">Seeing ones</h1>
      <p class="hero-subtitle">true nature</p>
      <p class="hero-copy">We love the slide, since majority of our time we are wearing masks, especially when in our working premises, when our heart beats for something else. We want to reveal our self, our true nature, remove the mask and be whoever we truly are.</p>
    </div>
  </section>

  <div class="brand-lockup">
    <span class="brand-square"></span>
    <span class="brand-name">toravi</span>
  </div>

  <div class="team">
    <div class="portrait portrait--dark" role="img" aria-label="Illustrated team member portrait with hair bun and glasses"></div>
    <div class="portrait portrait--dark" role="img" aria-label="Illustrated team member portrait with beard and glasses"></div>
    <div class="portrait portrait--accent" role="img" aria-label="Illustrated team member portrait in pink with glasses"></div>
    <div class="portrait portrait--dark" role="img" aria-label="Illustrated team member portrait with short hair and glasses"></div>
  </div>
</body>
</html>
```